Need Business Card for our Real Estate Business with Sales Executive's Picture

PANTONE 484 C ( RED)

PANTONE 2766 C ( BLUE

Industry/Entity Type

Real Estate

Contact Information for Business Card

Name, Mobile, email, & picture of Person
Agency Phone, address, Web address

Requirements
Must have
• Our Logo Colours, Agent Picture,

```html
<!DOCTYPE html>
<html lang="en">
<head>
<meta charset="utf-8">
<title>Kestra Real Estate – Business Card</title>
<link rel="stylesheet" href="https://fonts.googleapis.com/css2?family=Source+Sans+3:wght@400;600;700&display=swap">
<style>
  :root {
    --navy: #0c1538;
    --white: #ffffff;
    --red: #8a1c22;
    --grey-text: #7a7a7a;
    --photo-a: #e9e6df;
    --photo-b: #2a4a8f;
    --bg-light: #d8d8d8;
    --bg-dark: #6e6e6e;
  }
  * { box-sizing: border-box; margin: 0; padding: 0; }
  html, body { width: 1200px; height: 1200px; overflow: hidden; }
  body {
    background: radial-gradient(ellipse at 50% 45%, var(--bg-light) 0%, #a9a9a9 60%, var(--bg-dark) 100%);
    font-family: "Source Sans 3", sans-serif;
    position: relative;
  }
  .card {
    position: absolute;
    left: 170px;
    width: 860px;
    height: 513px;
    box-shadow: 0 10px 28px rgba(0,0,0,0.35);
    overflow: hidden;
  }
  .card--front { top: 47px; background: var(--white); }
  .card--back { top: 640px; background: var(--navy); }

  .brand {
    position: absolute;
    display: flex;
    align-items: center;
    gap: 14px;
    font-weight: 600;
    letter-spacing: 0.08em;
    white-space: nowrap;
  }
  .brand__mark { width: 18px; height: 18px; background: var(--red); flex: none; }
  .brand__name { font-size: 40px; line-height: 1; }
  .card--front .brand { left: 90px; top: 190px; color: var(--navy); }
  .card--back .brand { left: 50%; top: 50%; transform: translate(-50%, -50%); color: var(--white); }
  .card--back .brand__name { font-size: 50px; }

  .agent {
    position: absolute;
    left: 581px;
    top: 47px;
    width: 220px;
    text-align: center;
  }
  .agent__photo {
    width: 220px;
    height: 220px;
    border-radius: 50%;
    background: linear-gradient(180deg, var(--photo-a) 0%, var(--photo-a) 45%, var(--photo-b) 100%);
  }
  .agent__name {
    margin-top: 10px;
    font-size: 28px;
    font-weight: 700;
    color: var(--navy);
    line-height: 1.1;
  }
  .agent__role {
    font-size: 17px;
    color: var(--grey-text);
    letter-spacing: 0.04em;
  }

  .contact-band {
    position: absolute;
    left: 0; right: 0; bottom: 0;
    height: 163px;
    background: var(--navy);
    color: var(--white);
    font-size: 24px;
    font-weight: 400;
    display: flex;
    flex-direction: column;
    align-items: center;
    justify-content: center;
    gap: 6px;
  }
  .contact-row { display: flex; gap: 36px; line-height: 1.2; }
  .contact-row--address { margin-top: 12px; }
  .contact-item { display: flex; align-items: center; gap: 10px; }
  .icon { width: 20px; height: 20px; fill: var(--white); flex: none; }
</style>
</head>
<body>

<section class="card card--front">
  <div class="brand">
    <span class="brand__mark"></span>
    <span class="brand__name">KESTRA REAL ESTATE</span>
  </div>

  <div class="agent">
    <div class="agent__photo" role="img" aria-label="Portrait photo of the agent in a blue suit"></div>
    <p class="agent__name">Arjun Malhotra</p>
    <p class="agent__role">DIRECTOR</p>
  </div>

  <div class="contact-band">
    <div class="contact-row">
      <span class="contact-item">
        <svg class="icon" viewBox="0 0 20 20" aria-hidden="true"><path d="M5 1h10a1 1 0 0 1 1 1v16a1 1 0 0 1-1 1H5a1 1 0 0 1-1-1V2a1 1 0 0 1 1-1zm1 2v12h8V3zm4 13.2a1 1 0 1 0 0 .01z"/></svg>
        (000) 000-0000
      </span>
      <span class="contact-item">
        <svg class="icon" viewBox="0 0 20 20" aria-hidden="true"><path d="M1 7c0-2 4-4 9-4s9 2 9 4v2h-4V7.5c-1-.5-3-.8-5-.8s-4 .3-5 .8V9H1zm4 3h10l2 7H3zm5 1.5a2.5 2.5 0 1 0 0 5 2.5 2.5 0 0 0 0-5z"/></svg>
        (000) 000-0000
      </span>
    </div>
    <div class="contact-row">
      <span class="contact-item">
        <svg class="icon" viewBox="0 0 20 20" aria-hidden="true"><path d="M10 1l9 7v10H1V8zm0 2.4L3 8.8l7 4.8 7-4.8zM3 10.8V16h14v-5.2l-7 4.8z"/></svg>
        arjun.malhotra@email.com
      </span>
      <span class="contact-item">
        <svg class="icon" viewBox="0 0 20 20" aria-hidden="true"><path d="M10 2l9 8h-3v8h-4v-5H8v5H4v-8H1z"/></svg>
        www.domain.com
      </span>
    </div>
    <div class="contact-row contact-row--address">
      <span>Unit 8/145 Harbour Rd, Westfield, VIC 3150</span>
    </div>
  </div>
</section>

<section class="card card--back">
  <div class="brand">
    <span class="brand__mark"></span>
    <span class="brand__name">KESTRA REAL ESTATE</span>
  </div>
</section>

</body>
</html>
```